Modern Billboard Ad for Criminal Defense Firm

10.5 x 36 We're looking for something to set us apart from the local competition. Looking for sleek and modern. We're a mid-sized firm in a small market city. We want to give the artist room to be creative on this one.
Thanks

Target Market(s)

Adult clients who have been charged with a crime/DWI

Industry/Entity Type

legal

Font styles to use
Serif
Sans Serif

Requirements
Must have
• Needs to have the firm name in large lettering. Law Offices of Martin G Ashby. “PLLC” does not have to be included. Phone number of (555) 318-4092 should be included but not the main focus.
Nice to have
• A call to action or something similar. “Don’t go it alone, call today.”, “ Arrested?”

```html
<!DOCTYPE html>
<html lang="en">
<head>
<meta charset="utf-8">
<title>Martin G Ashby Billboard</title>
<link rel="stylesheet" href="https://fonts.googleapis.com/css2?family=Libre+Baskerville&family=Montserrat:wght@600&display=swap">
<style>
  :root {
    --page-bg: #e9ebef;
    --board-magenta: #7a1246;
    --board-deep: #2a0f2e;
    --board-navy: #10183c;
    --light-red: rgba(214, 40, 90, 0.55);
    --light-blue: rgba(70, 90, 230, 0.55);
    --ink-white: #ffffff;
    --badge-navy: #1d2f66;
    --badge-blue: #2f8fd0;
    --portrait-light: #9a9a9a;
    --portrait-dark: #2b2b2b;
  }
  html, body {
    margin: 0;
    width: 1200px;
    height: 675px;
    overflow: hidden;
    background: var(--page-bg);
  }
  .billboard {
    position: absolute;
    left: 20px;
    top: 168px;
    width: 1160px;
    height: 338px;
    overflow: hidden;
    background:
      radial-gradient(ellipse 260px 160px at 58% 55%, var(--light-red), transparent 70%),
      radial-gradient(ellipse 300px 170px at 82% 50%, var(--light-blue), transparent 70%),
      linear-gradient(90deg, var(--board-magenta) 0%, var(--board-deep) 45%, var(--board-navy) 100%);
  }
  .scene-backdrop {
    position: absolute;
    inset: 0;
  }
  .award-badge {
    position: absolute;
    left: 17px;
    top: 44px;
    width: 94px;
    height: 134px;
    background: linear-gradient(180deg, var(--badge-navy) 0%, var(--badge-navy) 82%, var(--badge-blue) 82%);
    border: 2px solid var(--ink-white);
    box-sizing: border-box;
  }
  .attorney-portrait {
    position: absolute;
    left: 8px;
    top: 40px;
    width: 380px;
    height: 298px;
    background: linear-gradient(180deg, var(--portrait-light) 0%, var(--portrait-dark) 100%);
  }
  .message {
    position: absolute;
    left: 430px;
    right: 20px;
    top: 0;
    bottom: 0;
    text-align: center;
    color: var(--ink-white);
  }
  .firm-label {
    position: absolute;
    left: 0; right: 0;
    top: 30px;
    display: flex;
    justify-content: center;
    align-items: center;
    gap: 14px;
    font-family: "Libre Baskerville", serif;
    font-size: 32px;
    letter-spacing: 1px;
  }
  .firm-label .rule {
    width: 62px;
    height: 2px;
    background: var(--ink-white);
  }
  .firm-name {
    position: absolute;
    left: 0; right: 0;
    top: 72px;
    margin: 0;
    font-family: "Libre Baskerville", serif;
    font-weight: 400;
    font-size: 72px;
    line-height: 1;
  }
  .call-to-action {
    position: absolute;
    left: 0; right: 0;
    top: 180px;
    font-family: "Montserrat", sans-serif;
    font-weight: 600;
    font-size: 56px;
    line-height: 1;
    letter-spacing: 2px;
    color: rgba(255,255,255,0.15);
    -webkit-text-stroke: 2px var(--ink-white);
  }
  .phone {
    position: absolute;
    left: 0; right: 0;
    top: 254px;
    font-family: "Libre Baskerville", serif;
    font-size: 54px;
    line-height: 1;
    letter-spacing: 14px;
  }
</style>
</head>
<body>
  <section class="billboard">
    <div class="scene-backdrop" role="img" aria-label="Photo of handcuffs under red and blue police lights"></div>
    <div class="attorney-portrait" role="img" aria-label="Black and white portrait of the attorney in a suit with jacket over shoulder"></div>
    <div class="award-badge" aria-hidden="true"></div>
    <div class="message">
      <div class="firm-label"><span class="rule"></span><span>LAW OFFICES OF</span><span class="rule"></span></div>
      <h1 class="firm-name">Martin G Ashby</h1>
      <div class="call-to-action">ARRESTED?</div>
      <div class="phone">(555) 318-4092</div>
    </div>
  </section>
</body>
</html>
```